Flyer-Design für Datenschutzorganisation
Zielgruppe
Unsere Zielgruppe sind mittelständische Unternehmen ohne Ärzte und Apotheken, Mitarbeiterzahl 1-100 Personen, wir unterstützen Unternehmer und Unternehmen bei der Umsetzung der EU-Datenschutzgrundverordnung im Betrieb, wir sind ein VORTA-zertifiziertes Beratungsunternehmen
Aufgabenstellung
'Unsere vornehmliche Aufgabe liegt im Aufbau und der Umsetzung einer praxisnahen und gesetzeskonformen Datenschutzorganisation in Ihrem Unternehmen.'
'Nur wer alle Regeln kennt, kann sie auch einhalten'
'Egal, ob aus Ressourcengründen oder um den Blick eines externen Experten zu erhalten – unsere Beratung macht Sinn. Im Mittelpunkt steht dabei immer Ihr Unternehmen, Ihre Mitarbeiter und Ihre Projekte.'
'Wir sorgen für eine datenschutzkonforme Ausgestaltung der Prozesse in Ihrem Unternehmen im Umgang mit personenbezogenen Daten, ausgerichtet an der Zielsetzung Ihres Geschäftsmodells. Sie erhalten somit ein Rundum-sorglos-Paket im Datenschutz.'

```html
<!DOCTYPE html>
<html lang="de">
<head>
<meta charset="utf-8">
<title>Flyer Datenschutzorganisation – Kobaltblau</title>
<link href="https://fonts.googleapis.com/css2?family=Roboto+Condensed:wght@300;400;700&family=Roboto:wght@400&display=swap" rel="stylesheet">
<style>
  :root{
    --navy:#1e2d54;
    --white:#ffffff;
    --paper:#ffffff;
    --ink:#111111;
  }
  *{margin:0;padding:0;box-sizing:border-box;}
  html,body{width:848px;height:1200px;overflow:hidden;background:var(--paper);}
  body{position:relative;font-family:"Roboto Condensed",Arial,sans-serif;color:var(--ink);}
  .sheet-format{position:absolute;left:52px;top:54px;font-family:"Roboto",Arial,sans-serif;font-size:19px;}
  .sheet-variant{position:absolute;left:0;width:848px;top:170px;text-align:center;font-family:"Roboto",Arial,sans-serif;font-size:18.5px;letter-spacing:.3px;}
  .flyer{position:absolute;left:215px;top:215px;width:430px;height:860px;background:var(--white);box-shadow:0 0 4px rgba(0,0,0,.25);}
  .flyer-main{position:absolute;left:0;top:0;width:430px;height:686px;background:var(--navy);color:var(--white);}
  .headline{position:absolute;left:15px;top:22px;font-weight:700;font-size:37px;line-height:36px;letter-spacing:-.2px;white-space:nowrap;}
  .copy{position:absolute;left:15px;font-weight:300;font-size:20.8px;line-height:24.6px;white-space:nowrap;}
  .copy b{font-weight:700;}
  .copy-1{top:117px;}
  .copy-2{top:241px;}
  .copy-3{top:388px;}
  .cert-badge{position:absolute;left:15px;top:560px;width:183px;height:76px;background:var(--white);}
  .cta{position:absolute;left:235px;top:587px;width:114px;height:114px;border-radius:50%;background:var(--white);box-shadow:0 3px 5px rgba(0,0,0,.35);display:flex;align-items:center;justify-content:center;}
  .cta-text{color:var(--navy);font-weight:700;font-size:18px;line-height:20px;text-align:center;transform:rotate(-8deg);}
  .brand{position:absolute;left:16px;top:724px;display:flex;align-items:center;gap:7px;}
  .brand-mark{width:15px;height:15px;background:var(--navy);}
  .brand-name{font-weight:700;font-size:26px;color:var(--navy);letter-spacing:.5px;}
  .web{position:absolute;left:16px;top:825px;font-weight:700;font-size:16px;color:var(--navy);}
  .contact{position:absolute;left:143px;top:722px;font-size:16.5px;line-height:17.4px;color:var(--navy);font-weight:400;font-style:normal;}
  .contact b{font-weight:700;}
  .contact .label{display:inline-block;width:56px;}
</style>
</head>
<body>
  <div class="sheet-format">Format: 105 mm x 210 mm</div>
  <div class="sheet-variant">KOBALTBLAU</div>

  <article class="flyer">
    <section class="flyer-main">
      <h1 class="headline">„MIT UNS SIND SIE<br>GUT BERATEN!“</h1>

      <p class="copy copy-1">Unsere vornehmliche Aufgabe liegt im <b>Aufbau</b><br>und der <b>Umsetzung</b> einer <b>praxisnahen</b> und<br><b>gesetzeskonformen Datenschutzorganisation</b><br>in Ihrem Unternehmen.</p>

      <p class="copy copy-2">Egal, ob aus Ressourcengründen oder um den<br><b>Blick eines externen Experten</b> zu erhalten –<br><b>unsere Beratung macht Sinn. Im Mittelpunkt</b><br>steht dabei immer <b>Ihr Unternehmen, Ihre Mit-<br>arbeiter</b> und <b>Ihre Projekte.</b></p>

      <p class="copy copy-3">Wir sorgen für eine <b>datenschutzkonforme Aus-<br>gestaltung der Prozesse</b> in Ihrem Unternehmen<br>im Umgang mit <b>personenbezogenen Daten,</b><br>ausgerichtet an der <b>Zielsetzung Ihres Geschäfts-<br>modells.</b> Sie erhalten somit ein Rundumsorglos-<br>Paket im Datenschutz.</p>

      <div class="cert-badge" role="img" aria-label="Platz für das Zertifizierungssiegel Datenschutzsystem"></div>
    </section>

    <div class="cta"><div class="cta-text">NEHMEN<br>SIE KONTAKT<br>MIT MIR<br>AUF!</div></div>

    <div class="brand"><span class="brand-mark"></span><span class="brand-name">KESSLER</span></div>

    <address class="contact">
      <b>Kessler Consulting GmbH</b><br>
      <b>Markus Kessler</b><br>
      Lindenweg 24<br>
      82049 Lindach bei München<br>
      Telefon: 089.55120947<br>
      Telefax: 089.5512099<br>
      <span class="label">E-Mail:</span>kontakt@kes-con.de
    </address>

    <div class="web">www.kes-con.de</div>
  </article>
</body>
</html>
```